Business Card Design Project

We need a Business Card for an Mechanical Engineering firm in Singapore. The design should be Modern & Technical looking, yet eye catching.

Our company deals in Cutting Tools & Machine Accessories for the Manufacturing Industries such as Oil & Gas, Aero Space, etc... For more information on our Company, you can either email me or view our website www.valtrion.com.sg.

We are trying to revamp our image to give our consumers a fresh new perspective to our company, so we welcome all ideas.

Industry/Entity Type

Business

Requirements
Must have
• Must incorporate New Company Logo into the card as shown in Uploaded file.

```html
<!DOCTYPE html>
<html lang="en">
<head>
<meta charset="utf-8">
<title>Valtrion Tools – Business Card</title>
<link rel="stylesheet" href="https://fonts.googleapis.com/css2?family=Arimo:wght@400;700&display=swap">
<style>
  :root {
    --backdrop: #a4a4a4;
    --card: #f4f4f3;
    --crimson: #8e1530;
    --blush: #d596a8;
    --blush-soft: #f0d9e0;
    --ink: #2a2a2a;
    --ink-soft: #555555;
    --rule: #777777;
  }
  * { box-sizing: border-box; margin: 0; padding: 0; }
  html, body { width: 1200px; height: 720px; overflow: hidden; }
  body {
    background: var(--backdrop);
    font-family: "Arimo", Arial, sans-serif;
    display: flex;
    align-items: center;
    justify-content: center;
    gap: 40px;
  }
  .card {
    position: relative;
    width: 540px;
    height: 309px;
    background: var(--card);
    box-shadow: 0 6px 18px rgba(0,0,0,.25);
    overflow: hidden;
  }

  /* Front */
  .card--front { display: flex; align-items: center; justify-content: center; }
  .brand {
    display: flex;
    align-items: center;
    gap: 14px;
    color: var(--crimson);
    font-weight: 700;
    text-transform: uppercase;
    letter-spacing: 1px;
  }
  .brand__dot {
    background: var(--crimson);
    border-radius: 50%;
    flex: none;
  }
  .card--front .brand { font-size: 38px; }
  .card--front .brand__dot { width: 34px; height: 34px; }

  /* Back */
  .holder {
    position: absolute;
    left: 46px;
    top: 40px;
    display: flex;
    align-items: center;
    gap: 12px;
  }
  .holder__name { color: var(--crimson); font-size: 31px; font-weight: 400; }
  .holder__divider { width: 2px; height: 28px; background: var(--rule); }
  .holder__role { color: var(--ink); font-size: 14px; margin-top: 10px; }

  .decor-band {
    position: absolute;
    left: 0;
    top: 150px;
    width: 210px;
    height: 78px;
    background: linear-gradient(90deg, var(--blush), var(--blush-soft));
  }

  .card--back .brand {
    position: absolute;
    right: 36px;
    top: 150px;
    font-size: 17px;
    gap: 8px;
  }
  .card--back .brand__dot { width: 16px; height: 16px; }

  .address {
    position: absolute;
    left: 120px;
    top: 238px;
    width: 220px;
    display: flex;
    align-items: flex-start;
    gap: 8px;
    color: var(--ink-soft);
    font-size: 13px;
    line-height: 1.3;
  }
  .contacts {
    position: absolute;
    left: 362px;
    top: 216px;
    list-style: none;
    color: var(--ink-soft);
    font-size: 13px;
    line-height: 1.5;
  }
  .contacts li { display: flex; align-items: center; gap: 8px; }
  .icon { width: 13px; height: 13px; fill: var(--ink-soft); flex: none; }
  .address .icon { margin-top: 2px; }
</style>
</head>
<body>

  <section class="card card--front" aria-label="Card front">
    <div class="brand">
      <span class="brand__dot"></span>
      <span class="brand__name">Valtrion Tools</span>
    </div>
  </section>

  <section class="card card--back" aria-label="Card back">
    <div class="holder">
      <span class="holder__name">Daniel Marsh</span>
      <span class="holder__divider"></span>
      <span class="holder__role">Managing Director</span>
    </div>

    <div class="decor-band" role="img" aria-label="Soft pink decorative area"></div>

    <div class="brand">
      <span class="brand__dot"></span>
      <span class="brand__name">Valtrion Tools</span>
    </div>

    <div class="address">
      <svg class="icon" viewBox="0 0 16 16" aria-hidden="true"><path d="M8 1 0 8h2v7h4v-5h4v5h4V8h2z"/></svg>
      <span>Abc town, 0 Street, New York<br>USA</span>
    </div>

    <ul class="contacts">
      <li>
        <svg class="icon" viewBox="0 0 16 16" aria-hidden="true"><path d="M4 0h8a1 1 0 0 1 1 1v14a1 1 0 0 1-1 1H4a1 1 0 0 1-1-1V1a1 1 0 0 1 1-1zm1 2v10h6V2zm3 11a1 1 0 1 0 0 2 1 1 0 0 0 0-2z"/></svg>
        000-000-0000
      </li>
      <li>
        <svg class="icon" viewBox="0 0 16 16" aria-hidden="true"><path d="M3.6 1 6 4.4 4.6 6.2a9 9 0 0 0 5.2 5.2L11.6 10 15 12.4 13.6 15C7 15 1 9 1 2.4z"/></svg>
        000-000-0000
      </li>
      <li>
        <svg class="icon" viewBox="0 0 16 16" aria-hidden="true"><path d="M0 3h16v10H0zm1.5 1.5v.3L8 9l6.5-4.2v-.3zm0 2v5h13v-5L8 10.7z"/></svg>
        info@valtrion.com.sg
      </li>
      <li>
        <svg class="icon" viewBox="0 0 16 16" aria-hidden="true"><circle cx="8" cy="8" r="7.5"/></svg>
        www.valtrion.com.sg
      </li>
    </ul>
  </section>

</body>
</html>
```